Corvane Photography Business Card Design

I need a business card designed for a photography business based in Perth, Western Australia called Corvane Photography.

We specialise in wedding, event photography and portrait photography.

The business card must borrow the style of the attached logo.

The hex codes for the colours in the logo are:
#ED1D85 - Pink
#89C23E - Green
#37282F - Black

The name on the card will be:
Name: Teodric
Phone: 0417360825
Website: www.corvanephotography-example.com.au
Facebook: corvanephotography

I am open and happy to accept creative concepts.

Industry/Entity Type

Business

```html
<!DOCTYPE html>
<html lang="en">
<head>
<meta charset="utf-8">
<title>Corvane Photography – Business Card</title>
<link href="https://fonts.googleapis.com/css2?family=Josefin+Sans:wght@300;400;600&display=swap" rel="stylesheet">
<style>
  :root {
    --pink: #ED1D85;
    --green: #89C23E;
    --ink: #37282F;
    --card: #ffffff;
    --backdrop: #e7e6e4;
    --shadow: rgba(55, 40, 47, 0.18);
  }
  * { box-sizing: border-box; margin: 0; padding: 0; }
  html, body {
    width: 1200px;
    height: 873px;
    overflow: hidden;
    background: var(--backdrop);
    font-family: "Josefin Sans", sans-serif;
    color: var(--ink);
  }
  .canvas {
    position: relative;
    width: 1200px;
    height: 873px;
  }
  .card {
    position: absolute;
    top: 126px;
    width: 380px;
    height: 620px;
    background: var(--card);
    box-shadow: 0 14px 34px var(--shadow);
    overflow: hidden;
  }
  .card--contact { left: 180px; }
  .card--brand { left: 640px; }

  /* Contact side */
  .contact-block {
    position: absolute;
    top: 150px;
    right: 118px;
    writing-mode: vertical-rl;
    display: flex;
    flex-direction: column;
    align-items: flex-start;
    gap: 8px;
  }
  .contact-name {
    font-weight: 600;
    font-size: 20px;
    letter-spacing: 4px;
    text-transform: uppercase;
  }
  .contact-phone {
    font-weight: 300;
    font-size: 21px;
    letter-spacing: 5px;
  }
  .rule {
    width: 2px;
    height: 150px;
    background: var(--ink);
    margin: 8px 4px;
  }
  .contact-link {
    font-weight: 400;
    font-size: 11px;
    letter-spacing: 1.5px;
    text-transform: uppercase;
  }

  /* Brand side */
  .brand-block {
    position: absolute;
    top: 40px;
    left: 150px;
    writing-mode: vertical-rl;
    display: flex;
    flex-direction: column;
    align-items: flex-start;
    gap: 6px;
  }
  .brand-name {
    font-weight: 300;
    font-size: 17px;
    letter-spacing: 9px;
    text-transform: uppercase;
    line-height: 1.2;
  }
  .brand-block .rule { height: 110px; margin: 10px 2px; }
  .brand-mark {
    position: absolute;
    right: -90px;
    bottom: -40px;
  }
</style>
</head>
<body>
<main class="canvas">
  <section class="card card--contact" aria-label="Business card, contact side">
    <div class="contact-block">
      <p class="contact-name">Teodric</p>
      <p class="contact-phone">04 1736 0825</p>
      <div class="rule"></div>
      <p class="contact-link">www.corvanephotography-example.com.au</p>
      <p class="contact-link">follow.example/corvanephotography</p>
    </div>
  </section>

  <section class="card card--brand" aria-label="Business card, brand side">
    <div class="brand-block">
      <h1 class="brand-name">Corvane<br>Photography</h1>
      <div class="rule"></div>
    </div>
    <svg class="brand-mark" width="300" height="300" viewBox="0 0 300 300" aria-hidden="true">
      <circle cx="150" cy="150" r="140" fill="var(--pink)"/>
    </svg>
  </section>
</main>
</body>
</html>
```